Video Sharing Site

UPDATE 2: Thanks to everyone who has submitted so far. I have decided to include 2nd and 3rd prizes are well, and I believe with a robust price. If you chose to participate, I will be working with the 2nd and 3rd prize winners also to use your selected designs to complete the rest of the webpages as specified in the brief.

-

UPDATE 1: The key is attractive, SOPHISTICATED yet roomy.

You are free to use any software package you like ie. Joomla, Drupal, Wordpress etc. We just need access to the HTML/CSS.

-

Hello everyone.

We require the HTML/CSS for a video sharing website. Our website is called VidLoomary.com. Think of a unique logo. However this is not the main focus. I will try to give you as much info about the website design as I can:

# Home page:
- with categories in sidebar
- video listings eg. popular, most viewed, etc.
- perhaps make promoted videos stand out

# simple login page

# User Profile page
- user details
- user uploaded videos
- profile comments

# User Profile Edit page

# User Profile Inbox page
- mock messages

# Search page
- list of videos that match search
- number of results
- pagination
- etc.

# Video page
- page where we are watching a video
- related videos
- video comments
- video description
- ratings (thumbs up/down)
- views
- tags
- etc.

# Video Categories page
- list of a few categories eg. newest, most viewed, highest rated, etc.
- with 10-15 videos under each

# Video Upload page with form

# About Us
- with subcategories in sidebar (different design to video categories in home page sidebar)

# Contact Us

# Header
- as any website an attractive search bar should accompany the header
- quick shortlinks to logged-in user eg. (5) comments, (3) inbox, logout, etc.

# Footer
- should be thick so that it can accommodate links to more specific (mock) web pages.

# General
- please be sure to include advertising
- Don't be afraid to use bold colors.
- I will not be selecting designs that are overly dark
- be sure that any page where video thumbnails are shown are accompanied by video rating, number of views and author.
- think about loading times as well. Avoid the use of large graphics where possible.

########### HINT ##########
The first two designs that I pick will be two different types:
- colorful
- quite conservative. Plenty of white with light greys
###########################

Thanks everybody who submits!

2nd and 3rd prized now included!

Just to keep you all updated. I have made a few changes to the brief. Mostly just to make it easier for you to gauge what I'm after.

I have received enough designs with blue in it. Please submit designs where blue is not a main color. Thank you all!

Software

• A sophisticated layout. It must look like a professional video sharing website.

```html
<!DOCTYPE html>
<html lang="en">
<head>
<meta charset="utf-8">
<title>VidLoomary.com – The Video Sharing Website</title>
<link href="https://fonts.googleapis.com/css2?family=Arimo:wght@400;700&family=Nunito+Sans:wght@300;400&display=swap" rel="stylesheet">
<style>
:root{
  --green:#5ea816;
  --green-light:#7cc62a;
  --green-dark:#4a8a0e;
  --ink:#222;
  --text:#333;
  --muted:#666;
  --line:#cfcfcf;
  --panel:#f0f0f0;
  --panel-dark:#e2e2e2;
  --bar:#2b2b2b;
  --footer:#2a2a2a;
  --star:#f0a020;
  --red:#e0392b;
}
*{box-sizing:border-box;margin:0;padding:0}
html,body{width:1200px;height:2286px;overflow:hidden}
body{position:relative;background:#fff;font-family:"Arimo",Arial,sans-serif;color:var(--text);font-size:13px}
.abs{position:absolute}
a{color:inherit;text-decoration:none}

/* header */
.site-header{left:0;top:0;width:1200px;height:212px;background:linear-gradient(#fff 0,#f4f4f4 55%,#e4e4e4 100%);border-bottom:1px solid #d4d4d4}
.brand{left:64px;top:44px;font-family:"Nunito Sans",Arial,sans-serif;font-weight:300;font-size:44px;color:#3a3a3a;letter-spacing:.5px}
.tagline{left:308px;top:34px;font-size:13px;font-style:italic;font-weight:700;color:#999}
.user-links{left:866px;top:32px;font-size:14px;color:#333;display:flex;gap:10px;align-items:center}
.user-links .ico{width:16px;height:16px;border-radius:50%;background:#f0b020;display:inline-block;vertical-align:middle;margin-right:6px}
.user-links .ico.help{background:#3b8fd8}
.sep{color:#999}
.tab-row{left:42px;top:140px;display:flex;gap:8px}
.tab{height:28px;padding:0 18px;line-height:28px;font-size:15px;background:linear-gradient(#fafafa,#dedede);border:1px solid #cfcfcf;color:#333}
.tab.active,.btn-green{background:linear-gradient(var(--green-light),var(--green));color:#fff;border-color:var(--green-dark)}
.main-nav{left:642px;top:122px;display:flex;gap:12px}
.main-nav a{height:46px;width:92px;text-align:center;line-height:46px;font-size:18px;background:linear-gradient(#fafafa,#d6d6d6);border:1px solid #c6c6c6;color:#333}
.main-nav a.active{background:linear-gradient(var(--green-light),var(--green));color:#fff;border-color:var(--green-dark)}
.search{left:42px;top:176px;width:410px;height:25px;border:1px solid #c8c8c8;background:#fff}
.search svg{position:absolute;left:6px;top:4px}
.btn-green{position:absolute;height:25px;line-height:23px;text-align:center;font-size:15px;border:1px solid var(--green-dark)}

/* video player */
.player{left:42px;top:229px;width:739px;height:335px;background:#111}
.player-screen{position:absolute;left:0;top:0;width:100%;height:282px;background:radial-gradient(ellipse at 55% 45%,#6a2a4a 0,#4a1238 40%,#1c0a16 100%)}
.player-top{position:absolute;top:10px;left:230px;display:flex;gap:34px;font-size:11px;color:#ddd;letter-spacing:.5px}
.play-btn{position:absolute;left:318px;top:110px}
.player-bar{position:absolute;left:0;top:282px;width:100%;height:53px;background:linear-gradient(#2c2c2c,#141414);color:#ddd;font-size:12px}
.progress{position:absolute;left:0;top:0;width:100%;height:4px;background:#444}
.progress i{display:block;width:64px;height:4px;background:#ddd}
.ctrl{position:absolute;left:28px;top:22px;display:flex;gap:14px;color:#eee;font-size:12px}
.player-actions{position:absolute;right:12px;top:22px;display:flex;gap:24px}
.player-actions span b{color:var(--green-light);margin-right:5px}
.player-shadow{left:62px;top:566px;width:700px;height:22px;background:radial-gradient(ellipse at 50% 0,rgba(0,0,0,.22),rgba(0,0,0,0) 70%)}

.thumb{background:#888;position:relative}
.t-hero{background:linear-gradient(135deg,#7a1a1a,#2a1418 55%,#c4621a)}
.t-poster{background:linear-gradient(160deg,#c45a10,#5a1a08 60%,#1a0c08)}
.t-news{background:linear-gradient(135deg,#9fd0f0,#e8f4fb 55%,#6aa4cc)}
.t-music{background:linear-gradient(135deg,#0e2a2e,#2a5a6a 55%,#0a1418)}
.t-portrait{background:linear-gradient(135deg,#6a2a4a,#2a0e20)}
.t-sport{background:linear-gradient(160deg,#8fbf5a,#e8e8e0 50%,#4a7a2a)}
.t-mic{background:linear-gradient(135deg,#0a2a5a,#2a6ab0 60%,#0a1a3a)}
.t-reflect{-webkit-box-reflect:below 2px linear-gradient(transparent 55%,rgba(255,255,255,.35))}

.strip .thumb{position:absolute}
.rule{left:42px;top:738px;width:739px;height:3px;background:#666}

/* panels */
.panel{background:var(--panel);border:1px solid var(--line)}
.featured{left:42px;top:762px;width:739px;height:257px}
.featured-label{position:absolute;left:0;top:0;width:48px;height:100%;background:var(--bar)}
.featured-label span{position:absolute;left:50%;top:50%;transform:translate(-50%,-50%) rotate(-90deg);white-space:nowrap;color:#fff;font-size:18px}
.arrow-btn{position:absolute;width:38px;height:38px;border-radius:50%;border:2px solid #bbb;background:#f8f8f8}
.featured .thumb{position:absolute}
.featured .card{position:absolute;top:158px}
.featured .card .title{margin-top:0}

.card .title{color:var(--green);font-size:17px;margin-top:8px}
.card .meta{font-size:13px;color:#333;margin-top:4px;white-space:nowrap}
.stars{color:var(--star);letter-spacing:-1px;font-size:13px;margin-right:4px}
.card .acts{font-size:13px;margin-top:6px;white-space:nowrap}
.plus{display:inline-block;width:12px;height:12px;position:relative;vertical-align:-1px;margin:0 4px 0 8px}
.plus:before,.plus:after{content:"";position:absolute;background:var(--red)}
.plus:before{left:4px;top:0;width:4px;height:12px}
.plus:after{left:0;top:4px;width:12px;height:4px}
.bubble{display:inline-block;vertical-align:-2px;margin-left:6px}

.bar-head{background:linear-gradient(#3a3a3a,#1e1e1e);color:#fff;height:36px;line-height:36px;font-size:17px;padding-left:12px}
.circle-plus{display:inline-block;width:18px;height:18px;border:2px solid #fff;border-radius:50%;text-align:center;line-height:13px;font-size:15px;margin-right:10px;vertical-align:-2px}
.recent-head{left:42px;top:1031px;width:739px}
.select{position:absolute;right:8px;top:6px;width:140px;height:24px;background:#fff;border:1px solid #bbb;color:#222;font-size:12px;line-height:22px;padding-left:6px}
.recent{left:42px;top:1067px;width:739px;height:280px;border-top:none}

.ad-tall{left:42px;top:1358px;width:187px;height:705px;background:linear-gradient(#7a5a3a 0,#33404a 40%,#1c2a33 70%,#8a9aa6 100%)}
.events{left:242px;top:1358px;width:539px;height:318px}
.event{position:absolute;left:40px;display:flex;gap:20px}
.event .thumb{width:120px;height:82px;flex:none}
.event .body{width:360px}
.event .title{color:var(--green);font-size:17px}
.event p{font-size:13px;line-height:17px;color:#333;margin-top:4px}

.banner{left:305px;top:1688px;width:857px;height:105px;background:#fff;border:1px solid #ddd}
.vendor-mark{position:absolute;left:22px;top:18px;display:flex;align-items:center;gap:8px;font-size:20px;color:#2a7ac8}
.vendor-mark i{width:60px;height:60px;border-radius:50%;border:3px solid #2a7ac8;display:block}

.mini{width:259px;height:261px}
.mini .card{padding:10px 16px}
.mini .thumb{width:226px;height:100px}

/* right column */
.side{left:794px;width:364px}
.side-head{height:44px;line-height:44px;text-align:center;font-size:19px;font-weight:700;background:linear-gradient(#fff,#e6e6e6);border-bottom:1px solid var(--line);position:relative;color:#111}
.side-head .tools{position:absolute;right:12px;top:0;font-size:13px;color:#555}
.pop-item{height:101px;border-bottom:1px solid var(--line);display:flex;gap:14px;padding:16px 10px 0 12px}
.pop-item .thumb{width:112px;height:72px;flex:none}
.pop-item .title{color:var(--green);font-size:17px}
.pop-item .meta{font-size:13px;margin-top:6px}
.pop-item .links{font-size:11px;margin-top:8px;white-space:nowrap}
.cat-list{list-style:none;padding:6px 0}
.cat-list li{height:35.5px;line-height:35.5px;padding-left:54px;font-size:15px;color:#444;border-bottom:1px dashed #cfcfcf;position:relative}
.cat-list li:last-child{border-bottom:none}
.cat-list li:before{content:"";position:absolute;left:30px;top:13px;border-left:7px solid #999;border-top:5px solid transparent;border-bottom:5px solid transparent}
.cat-list li:after{content:"";position:absolute;left:38px;top:13px;border-left:7px solid #999;border-top:5px solid transparent;border-bottom:5px solid transparent}
.green-head{color:var(--green)}

.footer{left:0;top:2077px;width:1200px;height:209px;background:var(--footer);color:#fff}
.fcol{position:absolute;top:20px}
.fcol h4{font-weight:400;font-size:15px;margin-bottom:16px}
.fcol li{list-style:none;font-size:12px;line-height:21px;color:#ddd}
.social{position:absolute;left:948px;top:146px;font-size:13px;display:flex;gap:6px;align-items:center}
.social i{width:18px;height:18px;background:#888;border-radius:3px;display:block}
</style>
</head>
<body>

<header class="site-header abs">
  <div class="brand abs">VidLoomary.com</div>
  <div class="tagline abs">The Video Sharing Website</div>
  <nav class="user-links abs">
    <a href="#"><span class="ico"></span>Free Register</a><span class="sep">|</span>
    <a href="#"><span class="ico"></span>Login</a><span class="sep">|</span>
    <a href="#"><span class="ico help"></span>Help</a>
  </nav>
  <div class="tab-row abs">
    <a class="tab active" href="#">Videos</a>
    <a class="tab" href="#">Categories</a>
    <a class="tab" href="#">Upload a Video</a>
  </div>
  <nav class="main-nav abs">
    <a class="active" href="#">Home</a><a href="#">Recents</a><a href="#">Top Video</a><a href="#">Upload</a><a href="#">Contact</a>
  </nav>
  <div class="search abs">
    <svg width="16" height="16" viewBox="0 0 16 16"><circle cx="6" cy="6" r="4.5" fill="none" stroke="#333" stroke-width="2"/><line x1="9.5" y1="9.5" x2="14" y2="14" stroke="#333" stroke-width="2.4"/></svg>
  </div>
  <a class="btn-green" style="left:465px;top:176px;width:116px" href="#">Video Search</a>
  <a class="btn-green" style="left:1044px;top:176px;width:114px" href="#">Register Now</a>
</header>

<section class="player abs">
  <div class="player-screen" role="img" aria-label="Featured video frame: portrait under a purple veil"></div>
  <div class="player-top"><span>▭ EMBED</span><span>⛶ FULLSCREEN</span><span>✉ SHARE</span></div>
  <svg class="play-btn" width="104" height="104" viewBox="0 0 104 104"><circle cx="52" cy="52" r="48" fill="rgba(0,0,0,.25)" stroke="rgba(255,255,255,.55)" stroke-width="4"/><path d="M40 30 L76 52 L40 74 Z" fill="rgba(255,255,255,.55)"/></svg>
  <div class="player-bar">
    <div class="progress"><i></i></div>
    <div class="ctrl"><span>◀</span><span>❚❚</span><span>▶</span></div>
    <div class="player-actions"><span><b>✚</b>Share</span><span><b style="color:#f08a20">◉</b>Suscribe</span><span><b style="color:#ccc">💬</b>Comments &nbsp;20</span></div>
  </div>
</section>
<div class="player-shadow abs"></div>

<div class="strip">
  <div class="thumb t-news t-reflect" role="img" aria-label="News anchor clip" style="left:76px;top:645px;width:93px;height:57px"></div>
  <div class="thumb t-hero t-reflect" role="img" aria-label="Action film still" style="left:183px;top:632px;width:109px;height:70px"></div>
  <div class="thumb t-portrait t-reflect" role="img" aria-label="Veiled portrait clip" style="left:326px;top:606px;width:152px;height:104px"></div>
  <div class="thumb t-poster t-reflect" role="img" aria-label="War film poster" style="left:512px;top:632px;width:110px;height:70px"></div>
  <div class="thumb t-hero t-reflect" role="img" aria-label="Action film still" style="left:640px;top:645px;width:93px;height:57px"></div>
</div>
<div class="rule abs"></div>

<section class="featured panel abs">
  <div class="featured-label"><span>Featured Videos</span></div>
  <div class="arrow-btn" style="left:56px;top:110px"><svg width="34" height="34" viewBox="0 0 34 34"><path d="M20 10 L12 17 L20 24" fill="none" stroke="#aaa" stroke-width="3"/></svg></div>
  <div class="arrow-btn" style="left:670px;top:110px"><svg width="34" height="34" viewBox="0 0 34 34"><path d="M14 10 L22 17 L14 24" fill="none" stroke="#aaa" stroke-width="3"/></svg></div>

  <div class="thumb t-hero" role="img" aria-label="Action film still" style="left:118px;top:19px;width:152px;height:107px"></div>
  <div class="thumb t-music" role="img" aria-label="Music video still" style="left:274px;top:9px;width:214px;height:138px"></div>
  <div class="thumb t-poster" role="img" aria-label="War film poster" style="left:493px;top:19px;width:152px;height:107px"></div>

  <div class="card" style="left:122px">
    <div class="title">Lorem ipsum</div>
    <div class="meta"><span class="stars">★★★★☆</span>(23600 views)</div>
    <div class="acts">Read More<span class="plus"></span>Share</div>
    <div class="acts">(20) Comments<svg class="bubble" width="20" height="14" viewBox="0 0 20 14"><path d="M2 1h16v9H8l-4 3v-3H2z" fill="#888"/></svg></div>
  </div>
  <div class="card" style="left:308px">
    <div class="title">Lorem ipsum</div>
    <div class="meta"><span class="stars">★★★★☆</span>(23600 views)</div>
    <div class="acts">Read More<span class="plus"></span>Share</div>
    <div class="acts">(20) Comments<svg class="bubble" width="20" height="14" viewBox="0 0 20 14"><path d="M2 1h16v9H8l-4 3v-3H2z" fill="#888"/></svg></div>
  </div>
  <div class="card" style="left:499px">
    <div class="title">Lorem ipsum</div>
    <div class="meta"><span class="stars">★★★★☆</span>(23600 views)</div>
    <div class="acts">Read More<span class="plus"></span>Share</div>
    <div class="acts">(20) Comments<svg class="bubble" width="20" height="14" viewBox="0 0 20 14"><path d="M2 1h16v9H8l-4 3v-3H2z" fill="#888"/></svg></div>
  </div>
</section>

<div class="recent-head bar-head abs"><span class="circle-plus">+</span>Recently Added
  <span style="position:absolute;right:160px;font-size:17px">Select Categories</span>
  <span class="select">Movies Trailers ▾</span>
</div>
<section class="recent panel abs">
  <div class="card abs" style="left:34px;top:24px">
    <div class="thumb t-hero t-reflect" role="img" aria-label="Action film still" style="width:152px;height:102px"></div>
    <div class="title" style="margin-top:34px">Lorem ipsum</div>
    <div class="meta"><span class="stars">★★★★☆</span>/ (236 views)</div>
    <div class="acts">Read More<span class="plus"></span>Share</div>
    <div class="acts">(20) Comments<svg class="bubble" width="20" height="14" viewBox="0 0 20 14"><path d="M2 1h16v9H8l-4 3v-3H2z" fill="#888"/></svg></div>
  </div>
  <div class="card abs" style="left:209px;top:24px">
    <div class="thumb t-poster t-reflect" role="img" aria-label="War film poster" style="width:152px;height:102px"></div>
    <div class="title" style="margin-top:34px">Lorem ipsum</div>
    <div class="meta"><span class="stars">★★★★☆</span>/ (236 views)</div>
    <div class="acts">Read More<span class="plus"></span>Share</div>
    <div class="acts">(20) Comments<svg class="bubble" width="20" height="14" viewBox="0 0 20 14"><path d="M2 1h16v9H8l-4 3v-3H2z" fill="#888"/></svg></div>
  </div>
  <div class="card abs" style="left:381px;top:24px">
    <div class="thumb t-news t-reflect" role="img" aria-label="News anchor clip" style="width:152px;height:102px"></div>
    <div class="title" style="margin-top:34px">Lorem ipsum</div>
    <div class="meta"><span class="stars">★★★★☆</span>/ (236 views)</div>
    <div class="acts">Read More<span class="plus"></span>Share</div>
    <div class="acts">(20) Comments<svg class="bubble" width="20" height="14" viewBox="0 0 20 14"><path d="M2 1h16v9H8l-4 3v-3H2z" fill="#888"/></svg></div>
  </div>
  <div class="card abs" style="left:554px;top:24px">
    <div class="thumb t-hero t-reflect" role="img" aria-label="Action film still" style="width:152px;height:102px"></div>
    <div class="title" style="margin-top:34px">Lorem ipsum</div>
    <div class="meta"><span class="stars">★★★★☆</span>/ (236 views)</div>
    <div class="acts">Read More<span class="plus"></span>Share</div>
    <div class="acts">(20) Comments<svg class="bubble" width="20" height="14" viewBox="0 0 20 14"><path d="M2 1h16v9H8l-4 3v-3H2z" fill="#888"/></svg></div>
  </div>
</section>

<aside class="ad-tall abs" role="img" aria-label="Advertisement: detective film poster, in cinemas, click to win"></aside>

<section class="events panel abs">
  <div class="bar-head"><span class="circle-plus">+</span>Latest Events<span style="position:absolute;right:14px;font-size:12px;color:#ccc">▼▲</span></div>
  <div class="event" style="top:46px">
    <div class="thumb t-mic t-reflect" role="img" aria-label="Live concert singer"></div>
    <div class="body">
      <div class="title">Lorem ipsum</div>
      <p>Dolor sit amet, consetetur sadipscing elitr, seddiam nonumy eirmod tempor. invidunt ut labore et dolore magna aliquyam erat, sed diam voluptua.</p>
      <div class="card"><div class="acts" style="margin-top:4px"><span class="stars">★★★★☆</span>/ (236 views) &nbsp;Read More<span class="plus"></span>Share</div><div class="acts" style="margin-top:4px">(20) Comments<svg class="bubble" width="20" height="14" viewBox="0 0 20 14"><path d="M2 1h16v9H8l-4 3v-3H2z" fill="#888"/></svg></div></div>
    </div>
  </div>
  <div class="event" style="top:180px">
    <div class="thumb t-hero t-reflect" role="img" aria-label="Action film still"></div>
    <div class="body">
      <div class="title">Lorem ipsum</div>
      <p>Dolor sit amet, consetetur sadipscing elitr, seddiam nonumy eirmod tempor. invidunt ut labore et dolore magna aliquyam erat, sed diam voluptua.</p>
      <div class="card"><div class="acts" style="margin-top:4px"><span class="stars">★★★★☆</span>/ (236 views) &nbsp;Read More<span class="plus"></span>Share</div><div class="acts" style="margin-top:4px">Comments this &nbsp;(20) Comments<svg class="bubble" width="20" height="14" viewBox="0 0 20 14"><path d="M2 1h16v9H8l-4 3v-3H2z" fill="#888"/></svg></div></div>
    </div>
  </div>
</section>

<aside class="banner abs">
  <div class="vendor-mark"><i></i>Vantex</div>
  <div style="position:absolute;left:160px;top:14px;font-size:25px;color:#d03a5a;line-height:29px">Call <b>1800 555 0142</b><br>today to buy your<br><span style="color:#555;font-size:22px">Strata™ R laptop</span></div>
  <div style="position:absolute;left:436px;top:16px;font-size:14px;color:#333">Starting at<br><span style="font-size:21px;line-height:36px">Rs. 29990*</span></div>
  <div style="position:absolute;left:560px;top:16px;width:88px;height:24px;border-radius:12px;background:#fff;border:1px solid #aaa;font-size:11px;text-align:center;line-height:22px;color:var(--red);font-weight:700">Call Now ›</div>
  <div style="position:absolute;left:566px;top:48px;font-size:11px;color:#888">Replay ↻</div>
  <div style="position:absolute;left:668px;top:12px;width:172px;height:58px;border:1px solid #ccc;font-size:18px;padding:6px 10px;line-height:22px">100% GENUINE<br><span style="font-size:15px">NovaOS 7</span></div>
  <div style="position:absolute;left:436px;top:84px;font-size:10px;color:#555">*Rollover for legal</div>
  <div style="position:absolute;left:590px;top:84px;font-size:10px;color:#555">Preinstalled with Genuine NovaOS 7 Home Basic</div>
</aside>

<section class="mini panel abs" style="left:242px;top:1802px">
  <div class="bar-head">Sports</div>
  <div class="card"><div class="thumb t-sport" role="img" aria-label="Cricket match"></div>
    <div class="title">Lorem ipsum</div><div class="meta"><span class="stars">★★★★☆</span>/ (236 views)</div>
    <div class="acts">Read More<span class="plus"></span>Share</div><div class="acts">(20) Comments<svg class="bubble" width="20" height="14" viewBox="0 0 20 14"><path d="M2 1h16v9H8l-4 3v-3H2z" fill="#888"/></svg></div></div>
</section>
<section class="mini panel abs" style="left:570px;top:1802px">
  <div class="bar-head">Music Videos</div>
  <div class="card"><div class="thumb t-music" role="img" aria-label="Music video still"></div>
    <div class="title">Lorem ipsum</div><div class="meta"><span class="stars">★★★★☆</span>/ (236 views)</div>
    <div class="acts">Read More<span class="plus"></span>Share</div><div class="acts">(20) Comments<svg class="bubble" width="20" height="14" viewBox="0 0 20 14"><path d="M2 1h16v9H8l-4 3v-3H2z" fill="#888"/></svg></div></div>
</section>
<section class="mini panel abs" style="left:899px;top:1802px">
  <div class="bar-head">Latest Movies</div>
  <div class="card"><div class="thumb t-hero" role="img" aria-label="Action film still"></div>
    <div class="title">Lorem ipsum</div><div class="meta"><span class="stars">★★★★☆</span>/ (236 views)</div>
    <div class="acts">Read More<span class="plus"></span>Share</div><div class="acts">(20) Comments<svg class="bubble" width="20" height="14" viewBox="0 0 20 14"><path d="M2 1h16v9H8l-4 3v-3H2z" fill="#888"/></svg></div></div>
</section>

<section class="side panel abs" style="top:225px;height:449px">
  <div class="side-head">Popular Videos<span class="tools">▼▲</span></div>
  <div class="pop-item"><div class="thumb t-portrait" role="img" aria-label="Veiled portrait clip"></div><div><div class="title">Lorem ipsum</div><div class="meta"><span class="stars">★★★★☆</span>/ (236 views)</div><div class="links">Read More / Give Comments / 20 Comments</div></div></div>
  <div class="pop-item"><div class="thumb t-music" role="img" aria-label="Music video still"></div><div><div class="title">Lorem ipsum</div><div class="meta"><span class="stars">★★★★☆</span>/ (236 views)</div><div class="links">Read More / Give Comments / 20 Comments</div></div></div>
  <div class="pop-item"><div class="thumb t-hero" role="img" aria-label="Action film still"></div><div><div class="title">Lorem ipsum</div><div class="meta"><span class="stars">★★★★☆</span>/ (236 views)</div><div class="links">Read More / Give Comments / 20 Comments</div></div></div>
  <div class="pop-item" style="border-bottom:none"><div class="thumb t-hero" role="img" aria-label="Action film still"></div><div><div class="title">Lorem ipsum</div><div class="meta"><span class="stars">★★★★☆</span>/ (236 views)</div><div class="links">Read More / Give Comments / 20 Comments</div></div></div>
</section>

<section class="side panel abs" style="top:701px;height:375px">
  <div class="side-head green-head">More Categories</div>
  <ul class="cat-list">
    <li>Comedy</li><li>Drama</li><li>Entertainment</li><li>Fashion &amp; Beauty</li><li>Food &amp; Drink</li><li>Health &amp; Fitness</li><li>Music Videos</li><li>News &amp; Politics</li><li>Sports &amp; Cars</li>
  </ul>
</section>

<aside class="side abs" style="top:1090px;height:301px;background:linear-gradient(135deg,#f0f0f0,#9a9a9a 55%,#3a3a3a)" role="img" aria-label="Advertisement: rock band concert promotion"></aside>

<section class="side panel abs" style="top:1406px;height:274px">
  <div class="bar-head">News<span style="position:absolute;right:14px;font-size:12px;color:#ccc">▼▲</span></div>
  <div class="pop-item" style="height:118px"><div class="thumb t-news t-reflect" role="img" aria-label="News anchor clip" style="width:118px;height:80px"></div><div class="card"><div class="title" style="margin-top:0">Lorem ipsum</div><div class="meta"><span class="stars">★★★★☆</span>/ (236 views)</div><div class="acts">Read More<span class="plus"></span>Share</div><div class="acts">(20) Comments<svg class="bubble" width="20" height="14" viewBox="0 0 20 14"><path d="M2 1h16v9H8l-4 3v-3H2z" fill="#888"/></svg></div></div></div>
  <div class="pop-item" style="height:118px;border-bottom:none"><div class="thumb t-news t-reflect" role="img" aria-label="News anchor clip" style="width:118px;height:80px"></div><div class="card"><div class="title" style="margin-top:0">Lorem ipsum</div><div class="meta"><span class="stars">★★★★☆</span>/ (236 views)</div><div class="acts">Read More<span class="plus"></span>Share</div><div class="acts">(20) Comments<svg class="bubble" width="20" height="14" viewBox="0 0 20 14"><path d="M2 1h16v9H8l-4 3v-3H2z" fill="#888"/></svg></div></div></div>
</section>

<footer class="footer abs">
  <div class="fcol" style="left:101px"><h4>VidLoomary</h4><ul><li>About</li><li>Press</li><li>Jobs</li><li>Blog</li><li>All Videos</li></ul></div>
  <div class="fcol" style="left:290px"><h4>Participate</h4><ul><li>Advertise</li><li>Become a Motion Maker</li><li>Become an Official User</li><li>B2B Solution</li><li>VidLoomary Publishers</li></ul></div>
  <div class="fcol" style="left:537px"><h4>Help</h4><ul><li>Forums</li><li>FAQ</li><li>Contact</li><li>Family Filter On</li></ul></div>
  <div class="fcol" style="left:729px"><h4>Legal Terms</h4><ul><li>Terms of Use</li><li>Privacy Policy</li><li>Prohibited Content</li><li>Copyright notification</li><li>Child Protection</li></ul></div>
  <div class="fcol" style="left:942px"><h4>Developers</h4><ul><li>Data API</li><li>Player API</li></ul></div>
  <div class="social">Follow us on: <i></i><i></i><i></i></div>
</footer>

</body>
</html>
```